High Profile Branding Company Needs New WordPress Site (Corvale)

Our creative agency is looking for a new website.

We help small business owners develop their branding. We would like to see modern, clean designs that reflect our professional and upscale clientele.

Our color scheme is purple, and we are looking for a layout that makes much use of white and appears very clean while using our various shades of purple to accent and complete the site design.

Target Market(s)

Small business owners, 70% female and 30% male, North American, Doctors/dentists, lawyers, consultants, stylists, personal trainers, accountants, etc

Industry/Entity Type

Small Business

Requirements
Must have
• ***1) Attached PDF site layout***

We have assembled a rough idea of the site layout we have in mind as an attached PDF file, to guide you in your design process.

Please use this file as a starting point for your design ideas.

***2) Site Concept, Color Scheme, Logo & Font***

We would like this site to be very clean, primarily using white space and a clean background with the purple colors used for boxes, button, navigation bar, sidebar images, etc.

Kindly use the color scheme found in the attached JPEG.

We also ask you use the attached logo at the top left of the page.

Finally, we ask you use only the fonts Arial/Helvetica, along with variations of the Gotham font; found as an attached file.

***3) Use of “Circle” Pattern***

The attached “circle” pattern may be used to accent page backgrounds, buttons, etc. Please ensure this pattern is used lightly – such as faded into a background, etc.

***4) Top Right - Optin Box***

The top right of the layout should include a box with the text found in the attached “#5 Header Right” document.

This box will include a form to submit name and email in exchange for the downloadable files mentioned.

You may wish to design “eCovers” the audio CD, eBook, checklist, and newsletter.

***5) Top Right - Social Media Links***

Above this box, also at the top right of the layout, kindly include a graphic with our 800# and buttons that will link to Plimora, Quavet, Brontly, and our RSS feed.

***6) Homepage - Slideshow***

On the homepage layout, kindly note that there are several questions. Please include an appropriate image with each question (business people, profit chart, etc.) and use these images as a slideshow.

***7) Homepage – 3 Divisions***

Also note that on the homepage, there are three “divisions”. Each of these will link to a different page of the website upon completion. The text for each box can be found in the attached “#1 Homepage” document.

***8) Sidebar Buttons***

Kindly note that there will be 3 sidebar buttons used on the sidebar for each page of the layout. The text for each button can be found in the attached “#4 Sidebar Buttons” document.

Please use an appropriate image integrated into each button (e.g: a telephone for the “Brand Strategy Session” button.

***9) Founder’s Photo & Signature***

Please use our founder’s photo, attached to this brief. You may wish to use this brief as an image in the “Questions” sidebar button.

The attached founder’s signature may be used just below in the quote in the header left, as shown in the PDF layout draft.

***10) Corvale Framework***

We kindly ask that you base our site off the "Corvale" framework developed by Tindlecraft. You may base the theme off any of the child themes.
Should not have
• We would like to avoid a design that looks too busy or "flashy".

Please avoid anything that is cartoon-like in appearance.

Please do not apply a "3D/Glossy" effect to any buttons, or graphics.

```html
<!DOCTYPE html>
<html lang="en">
<head>
<meta charset="utf-8">
<title>The Vantora Agency</title>
<link href="https://fonts.googleapis.com/css2?family=Montserrat:wght@400;600;700&family=Arimo:wght@400;700&display=swap" rel="stylesheet">
<style>
:root{
  --purple-deep:#3a1262;
  --purple:#5b2590;
  --purple-mid:#6f34a6;
  --purple-light:#8a55c0;
  --ink:#2a2a2a;
  --white:#fff;
  --link:#1e88d8;
  --green:#8cc21f;
  --orange:#f07a10;
  --blue:#1a9ad6;
  --yellow:#ffd83a;
}
*{box-sizing:border-box;margin:0;padding:0}
html,body{width:1119px;height:1200px;overflow:hidden}
body{
  position:relative;
  font-family:"Arimo",Arial,sans-serif;
  color:var(--ink);
  background:linear-gradient(180deg,#4a1a7a 0%,#3a1262 45%,#5b2590 100%);
}
.abs{position:absolute}

/* header */
.header{left:113px;top:0;width:891px;height:207px;background:linear-gradient(#fff,#eeedf1);border:2px solid #c9bfd6;border-top:none}
.brand{left:34px;top:34px}
.brand-name{font-family:"Montserrat",sans-serif;font-weight:400;font-size:36px;letter-spacing:1px;color:var(--purple-deep);line-height:1}
.brand-tag{font-family:"Arimo",Arial,sans-serif;font-weight:400;font-size:13px;color:#666;margin-top:8px;letter-spacing:.5px}
.intro-quote{left:40px;top:105px;width:420px;font-size:11px;line-height:14px;color:#333;text-align:center}
.signature{left:330px;top:154px;width:110px;height:22px;background:linear-gradient(90deg,#ddd,#bbb);border-radius:3px}
.signer{left:348px;top:181px;font-size:11px;font-weight:700;color:#333}
.phone-line{right:34px;top:46px;display:flex;align-items:center;gap:10px}
.phone-number{font-size:17px;color:#333}
.social{display:flex;gap:3px}
.social span{width:13px;height:13px;border-radius:2px;background:var(--purple-mid)}
.optin{right:34px;top:76px;width:200px;text-align:right}
.optin-small{font-size:11px;color:#333}
.optin-title{font-size:20px;color:#333;margin-top:2px}
.field{display:block;width:196px;height:22px;margin:6px 0 0 auto;border:2px solid #c9c6cf;background:#fff;font-size:10px;font-style:italic;color:#888;padding:4px 6px;text-align:left}
.optin-btn{display:inline-block;margin-top:6px;background:var(--purple);color:#fff;font-size:12px;padding:4px 10px}

/* nav */
.nav{left:140px;top:222px;display:flex}
.nav a{color:#fff;font-size:13px;text-decoration:none;padding:4px 18px;margin-right:14px}
.nav a.current{background:var(--purple-light);border:1px solid #a77fd6}

/* main panel */
.main{left:113px;top:263px;width:891px;height:777px;background:linear-gradient(#dad7df,#fff 20%,#fff 80%,#dad7df);border:2px solid #b9a8cf}
.slider{left:33px;top:36px;width:542px;height:262px;border:3px solid #fff;box-shadow:0 0 0 1px #ccc;background:linear-gradient(160deg,#6a2da0,#3e0f68)}
.slider-art{left:0;top:0;width:100%;height:100%;background:radial-gradient(ellipse at 75% 75%,rgba(0,0,0,.35),transparent 55%)}
.slider-headline{left:48px;top:36px;width:370px;font-weight:700;font-size:17px;line-height:20px;color:#fff}
.dots{left:16px;top:240px;display:flex;gap:10px}
.dots span{width:7px;height:7px;border-radius:50%;background:#fff}
.dots span.on{background:var(--purple-light)}
.divider{left:33px;width:542px;height:6px;background:repeating-linear-gradient(90deg,#bbb 0 2px,transparent 2px 4px)}
.lead{left:33px;top:357px;width:520px;font-size:15px;line-height:19px;color:var(--purple-deep)}
.about{left:33px;top:409px;width:540px;font-size:10.5px;line-height:13px;color:#333}
.read-more{left:466px;top:467px;font-size:11px;color:var(--link)}
.goal{left:33px;top:524px;width:545px;font-family:"Montserrat",sans-serif;font-weight:700;font-size:15px;line-height:18px;color:var(--purple-deep)}

/* sidebar */
.side-btn{left:595px;width:263px;border:3px solid #fff;box-shadow:0 0 0 1px #ccc;background:linear-gradient(#6b2ea3,#3e0f68);color:#fff}
.side-pic{left:6px;top:10px;width:80px;height:100px;border-radius:3px}
.side-text{left:90px;top:10px;width:164px}
.side-title{font-family:"Montserrat",sans-serif;font-weight:700;font-size:14px;line-height:16px}
.side-body{font-size:10.5px;line-height:13px;margin-top:4px}
.side-cta{font-size:10.5px;font-style:italic;color:var(--yellow);margin-top:8px}

/* division cards */
.card{top:578px;width:257px;height:175px;border:3px solid #fff;box-shadow:0 0 0 1px #ccc;padding:14px 16px}
.card-title{font-family:"Montserrat",sans-serif;font-weight:700;font-size:15px;line-height:18px;min-height:40px}
.card ul{list-style:none;margin-top:2px}
.card li{font-size:11px;line-height:21px;color:#333;display:flex;align-items:center;gap:10px}
.card li svg{flex:none}
.card-link{position:absolute;right:28px;bottom:14px;font-family:"Montserrat",sans-serif;font-weight:700;font-size:11px;color:var(--link)}
.card.standout{left:38px;background:linear-gradient(#fff,#dbf0d5)}
.card.standout .card-title{color:var(--green)}
.card.stepup{left:316px;background:linear-gradient(#fff,#f8e6cf)}
.card.stepup .card-title{color:var(--orange)}
.card.results{left:595px;background:linear-gradient(#fff,#d6e6f5)}
.card.results .card-title{color:var(--blue)}

/* footer */
.foot-brand{left:117px;top:1062px}
.foot-brand .brand-name{font-size:16px;color:#fff}
.foot-brand .brand-tag{font-size:8px;margin-top:3px;color:#d9c9ee}
.foot-nav{right:118px;top:1066px;display:flex;font-size:11px;color:#fff}
.foot-nav span{padding:0 9px;border-left:1px solid #fff;line-height:11px}
.foot-nav span:first-child{border-left:none}
.foot-copy{right:118px;top:1088px;font-size:11px;color:#fff}
.foot-address{right:118px;top:1116px;text-align:right;font-size:11px;line-height:13px;color:#c9b6e3;font-style:normal}
</style>
</head>
<body>

<header class="header abs">
  <div class="brand abs">
    <div class="brand-name">THE VANTORA AGENCY</div>
    <div class="brand-tag">CLEAR BRANDS. STEADY GROWTH. REAL RESULTS.</div>
  </div>
  <p class="intro-quote abs">"At The Vantora Agency, we're leaders in helping small business owners, just like you, get results from their branding and online presence. Discover how our expertise and creativity can help you grow, lead, and reach the results you want."</p>
  <div class="signature abs" role="img" aria-label="Founder's handwritten signature"></div>
  <div class="signer abs">- Milo Brenner -</div>

  <div class="phone-line abs">
    <span class="phone-number">1-888-555-0147</span>
    <span class="social" aria-label="Social links: Plimora, Quavet, RSS, Brontly"><span></span><span></span><span></span><span></span><span></span></span>
  </div>
  <form class="optin abs">
    <div class="optin-small">Request Your Complimentary</div>
    <div class="optin-title">Brand Clarity Kit!</div>
    <span class="field">Your name here...</span>
    <span class="field">Your email here...</span>
    <span class="optin-btn">Send My Free Kit!</span>
  </form>
</header>

<nav class="nav abs">
  <a class="current">Home</a><a>The Agency</a><a>How We Can Help</a><a>Portfolio</a><a>Success Stories</a><a>Get Started Now</a>
</nav>

<main class="main abs">
  <section class="slider abs">
    <div class="slider-art abs" role="img" aria-label="Rising profit line chart with tumbling percentage dice"></div>
    <h2 class="slider-headline abs">Do you worry that your website, marketing materials, and branding fail to reflect your level of professionalism, skill, and service?</h2>
    <svg class="abs" style="left:6px;top:120px" width="20" height="20" viewBox="0 0 20 20"><circle cx="10" cy="10" r="9" fill="#fff"/><path d="M12 5 7 10l5 5" stroke="#333" stroke-width="2" fill="none"/></svg>
    <svg class="abs" style="right:6px;top:120px" width="20" height="20" viewBox="0 0 20 20"><circle cx="10" cy="10" r="9" fill="#fff"/><path d="M8 5l5 5-5 5" stroke="#333" stroke-width="2" fill="none"/></svg>
    <div class="dots abs"><span></span><span class="on"></span><span></span></div>
  </section>

  <div class="divider abs" style="top:334px"></div>
  <p class="lead abs">If the questions above resonate with you, you'll be glad to know that you're far from alone…and you're in the right place.</p>
  <p class="about abs">We're The Vantora Agency, a premier creative and consulting firm with a simple mission – to help small business owners like you get results through branding and online presence. It's about helping you stand out from your competition, step up your lead generation and marketing efforts, and shift your results quickly, so you can reach your business goals.</p>
  <span class="read-more abs">Read more &gt;&gt;</span>
  <div class="divider abs" style="top:502px"></div>
  <h3 class="goal abs">What's Your Goal? No matter what you're looking to achieve; we've got your ideal solution!</h3>

  <aside>
    <div class="side-btn abs" style="top:36px;height:151px">
      <div class="side-pic abs" role="img" aria-label="Telephone receiver above a 20 minute badge" style="background:linear-gradient(#4a4a4a,#8a8a8a)"></div>
      <div class="side-text abs">
        <div class="side-title">Schedule Your Brand Strategy Session</div>
        <div class="side-body">Let's take 20 minutes to discuss your brand and online presence, find solutions to your biggest frustrations, and discover the next steps to shift your results!</div>
        <div class="side-cta">Get started today! Click here!</div>
      </div>
    </div>
    <div class="side-btn abs" style="top:196px;height:150px">
      <div class="side-pic abs" role="img" aria-label="Portrait photo of the company founder" style="top:24px;height:90px;border:2px solid #c8b4e0;background:linear-gradient(#777,#333)"></div>
      <div class="side-text abs" style="top:20px">
        <div class="side-title">Questions?</div>
        <div class="side-body">Here's your chance get answers and to ask brand strategist and company president Milo Brenner your burning questions!</div>
        <div class="side-cta">Get the scoop by clicking here!</div>
      </div>
    </div>
    <div class="side-btn abs" style="top:356px;height:151px">
      <div class="side-pic abs" role="img" aria-label="Large blue percent symbol" style="background:linear-gradient(#5a8fd0,#2c4f9a)"></div>
      <div class="side-text abs">
        <div class="side-title">Just Imagine</div>
        <div class="side-body">Getting paid to tell your network know about The Vantora Agency, saving big on your design needs, or even getting our services at no cost! It's all possible with our VantoraAmbassador Program.</div>
        <div class="side-cta">Click to learn more!</div>
      </div>
    </div>
  </aside>

  <section class="card standout abs">
    <div class="card-title">You Want To Stand Out...</div>
    <ul>
      <li><svg width="9" height="8" viewBox="0 0 9 8"><path d="M1 4l2.5 2.5L8 1" stroke="#8cc21f" stroke-width="2" fill="none"/></svg>The Brand Clarity Kit</li>
      <li><svg width="9" height="8" viewBox="0 0 9 8"><path d="M1 4l2.5 2.5L8 1" stroke="#8cc21f" stroke-width="2" fill="none"/></svg>The Brand Exposure Service</li>
    </ul>
    <span class="card-link">IT BEGINS HERE &gt;&gt;</span>
  </section>
  <section class="card stepup abs">
    <div class="card-title">You're Ready To Step Up...</div>
    <ul>
      <li><svg width="9" height="8" viewBox="0 0 9 8"><path d="M1 4l2.5 2.5L8 1" stroke="#f07a10" stroke-width="2" fill="none"/></svg>The Vantora Brand Strategy Day</li>
      <li><svg width="9" height="8" viewBox="0 0 9 8"><path d="M1 4l2.5 2.5L8 1" stroke="#f07a10" stroke-width="2" fill="none"/></svg>The Accelerate Your Brand Service</li>
      <li><svg width="9" height="8" viewBox="0 0 9 8"><path d="M1 4l2.5 2.5L8 1" stroke="#f07a10" stroke-width="2" fill="none"/></svg>Vantora Brand Management</li>
    </ul>
    <span class="card-link">GET AHEAD &gt;&gt;</span>
  </section>
  <section class="card results abs">
    <div class="card-title">You 're Looking For<br>Big Results...</div>
    <ul>
      <li><svg width="9" height="8" viewBox="0 0 9 8"><path d="M1 4l2.5 2.5L8 1" stroke="#1a9ad6" stroke-width="2" fill="none"/></svg>The Complete Brand Makeover Service</li>
      <li><svg width="9" height="8" viewBox="0 0 9 8"><path d="M1 4l2.5 2.5L8 1" stroke="#1a9ad6" stroke-width="2" fill="none"/></svg>The Vantora Brand Strategy Day</li>
      <li><svg width="9" height="8" viewBox="0 0 9 8"><path d="M1 4l2.5 2.5L8 1" stroke="#1a9ad6" stroke-width="2" fill="none"/></svg>Premier Brand Management</li>
    </ul>
    <span class="card-link">MAKE THE SHIFT &gt;&gt;</span>
  </section>
</main>

<footer>
  <div class="foot-brand abs">
    <div class="brand-name">THE VANTORA AGENCY</div>
    <div class="brand-tag">CLEAR BRANDS. STEADY GROWTH. REAL RESULTS.</div>
  </div>
  <div class="foot-nav abs"><span>Home</span><span>The Agency</span><span>How We Can Help</span><span>Portfolio</span><span>Success Stories</span><span>Get Started Now</span></div>
  <div class="foot-copy abs">2011© Copyright Vantora Agency &nbsp; | &nbsp;All Rights Reserved</div>
  <address class="foot-address abs">
    118 Larkmoor Lane, Fenwick City<br>
    Northland 40211<br>
    Telp. 0200-5550173, Fax. 0200-5550174<br>
    Email: info@vantoraagency.com<br>
    website: www.vantoraagency.com
  </address>
</footer>

</body>
</html>
```